Wordpress theme for food/recipe blog - family friendly

I've recently setup a Wordpress site to document all my tried and tested recipes. However I'm not happy with the design and layout of the theme I got. See sunnyoventable.com

It's also lacking a header/identity/logo as well. I would like a theme which is eye catching, cute and easy to navigate bearing in mind that the site is meant to be a personal blog documenting my culinary journey.

I would definitely like a logo / cartoon of a chubby, dimpled specky girl in apron perhaps holding up some utensil to show what this blog is about. I cook mainly for my family comprising my husband and our little baby girl who is 16months.

I love making breads the most if that helps with the logo/header design.
Updates

Reason: need more designs

Target Market(s)

- family with young kids
- mummies
- amateur cooks
- people who love food/ baking and cooking and sharing recipes

Industry/Entity Type

Baby

Requirements
Must have
• - Viewable on mobile - ie must be mobile friendly
- header/image - when shared on social media the image will be the one that is identified by people/readers

```html
<!DOCTYPE html>
<html lang="en">
<head>
<meta charset="utf-8">
<title>Sunny Oven Table – Home Baked Daily</title>
<link rel="stylesheet" href="https://fonts.googleapis.com/css2?family=Oxygen:wght@400;700&family=Oswald:wght@500&family=PT+Sans:wght@400&display=swap">
<style>
:root{
  --cream:#fbe9e3;
  --header-bg:#fdf6f3;
  --brown:#4b2a12;
  --brown-text:#5a3218;
  --orange:#e0663a;
  --orange-deep:#d95a30;
  --rust:#c8502a;
  --green:#58a639;
  --white:#ffffff;
  --card-border:#f0d2c6;
  --body-text:#6b5a52;
  --dot:#c9b3aa;
  --footer-text:#f3dfd2;
  --footer-muted:#9a7b66;
}
*{box-sizing:border-box;margin:0;padding:0}
html,body{width:992px;height:1200px;overflow:hidden}
body{position:relative;background:var(--cream);font-family:"PT Sans",Tahoma,sans-serif;color:var(--body-text)}
.abs{position:absolute}

/* header */
.site-header{left:0;top:0;width:992px;height:185px;background:linear-gradient(#fbe8e0,var(--header-bg) 40%,#fff)}
.brand-dot{left:196px;top:40px;width:70px;height:70px;border-radius:50%;background:var(--orange)}
.brand-name{left:126px;top:100px;font-family:"Oxygen",sans-serif;font-weight:700;font-size:40px;color:var(--rust);letter-spacing:.5px;white-space:nowrap}
.brand-tagline{left:336px;top:146px;font-family:"PT Sans",sans-serif;font-size:15px;letter-spacing:4.5px;color:var(--brown);white-space:nowrap}

/* nav */
.main-nav{left:0;top:181px;width:992px;height:48px;background:var(--brown);border-top:4px solid #e6cfc2}
.scallop-down{left:0;top:227px;width:992px;height:8px;background:radial-gradient(circle at 5px 0,var(--brown) 4.5px,transparent 5px) repeat-x;background-size:10px 8px}
.nav-list{list-style:none;font-family:"Oxygen",sans-serif;font-size:15px;color:var(--white)}
.nav-list li{position:absolute;top:195px;white-space:nowrap}
.nav-list .is-current{left:139px;top:185px;width:61px;height:34px;background:var(--white);color:var(--brown);border-radius:5px 5px 0 0;text-align:center;line-height:34px}

/* hero */
.hero{left:0;top:230px;width:992px;height:363px;background:linear-gradient(var(--orange),var(--orange-deep))}
.feature-photo{left:118px;top:248px;width:495px;height:243px;border:6px solid var(--white);background:linear-gradient(120deg,#b9643c,#8c4a22 45%,#9bb66a 80%,#d7e9b4);overflow:hidden}
.ribbon{left:112px;top:246px;width:110px;height:110px;overflow:hidden}
.ribbon span{position:absolute;left:-34px;top:26px;width:150px;height:26px;background:var(--green);transform:rotate(-45deg);color:var(--white);font-family:"Oswald",sans-serif;font-size:15px;text-align:center;line-height:26px}
.thumb{width:118px;height:115px;border:3px solid #f5e0d2}
.thumb-1{left:624px;top:248px;background:linear-gradient(135deg,#8a4a2a,#9cc06a)}
.thumb-2{left:754px;top:248px;background:linear-gradient(135deg,#b58a60,#d9c3a4)}
.thumb-3{left:624px;top:375px;background:linear-gradient(135deg,#5a1d10,#b2381e)}
.thumb-4{left:754px;top:375px;background:linear-gradient(135deg,#d8cdbb,#b4301c 60%,#3a2a22)}
.hero-title{left:125px;top:497px;font-family:"Oxygen",sans-serif;font-size:23px;color:var(--white)}
.hero-text{left:125px;top:528px;width:460px;font-family:"Oxygen",sans-serif;font-size:14.4px;line-height:18px;color:var(--white)}

/* posts */
.post-card{left:126px;width:485px;height:233px;background:var(--white);border:1px solid var(--card-border)}
.date-badge{width:82px;height:82px}
.date-badge text{font-family:"Oswald",sans-serif;fill:var(--white)}
.post-title{font-family:"Oxygen",sans-serif;font-size:20px;color:var(--brown-text);white-space:nowrap}
.post-meta{font-family:"Oxygen",sans-serif;font-size:11px;color:var(--green);white-space:nowrap}
.post-meta b{font-weight:400;color:var(--brown-text)}
.post-photo{width:144px;height:118px;background:linear-gradient(160deg,#e4d4bd 0,#cdb89a 28%,#2d2420 32%,#b5301a 60%,#8c2412)}
.post-excerpt{width:250px;font-size:11.2px;line-height:18px;color:var(--body-text)}
.read-more{color:var(--orange)}

/* sidebar */
.widget-title{font-family:"Oxygen",sans-serif;font-size:20px;color:var(--brown-text)}
.widget-list{list-style:none;width:186px;font-size:11px;color:#4b3a32}
.widget-list li{position:relative;padding:4px 0 5px 18px;border-bottom:1px dotted var(--dot);line-height:13px}
.widget-list li::before{content:"";position:absolute;left:2px;top:7px;border-left:4px solid var(--orange);border-top:3px solid transparent;border-bottom:3px solid transparent}
.cat-list li{height:21.5px}
.archive-select{left:645px;top:1053px;width:175px;height:20px;background:var(--white);font-size:11px;line-height:20px;padding-left:6px;color:#333}
.archive-select .caret{position:absolute;right:0;top:0;width:24px;height:20px;background:#b8b0ad}
.archive-select .caret::after{content:"";position:absolute;left:7px;top:6px;border-top:8px solid var(--white);border-left:5px solid transparent;border-right:5px solid transparent}

/* footer */
.site-footer{left:0;top:1153px;width:992px;height:47px;background:var(--brown)}
.scallop-up{left:0;top:1146px;width:992px;height:8px;background:radial-gradient(circle at 5px 8px,var(--brown) 4.5px,transparent 5px) repeat-x;background-size:10px 8px}
.footer-nav{list-style:none;font-family:"Oxygen",sans-serif;font-size:11px;color:var(--footer-text)}
.footer-nav li{position:absolute;top:1165px;white-space:nowrap}
.copyright{right:120px;top:1166px;font-size:9.5px;color:var(--footer-muted)}
</style>
</head>
<body>

<header>
  <div class="abs site-header"></div>
  <div class="abs brand-dot"></div>
  <div class="abs brand-name">Sunny Oven Table</div>
  <div class="abs brand-tagline">HOME BAKED DAILY</div>
</header>

<nav>
  <div class="abs main-nav"></div>
  <div class="abs scallop-down"></div>
  <ul class="nav-list">
    <li class="is-current">Home</li>
    <li style="left:220px">About me</li>
    <li style="left:314px">Blog</li>
    <li style="left:378px">Kitchen Tips</li>
    <li style="left:489px">Recipes</li>
    <li style="left:575px">Contact</li>
  </ul>
</nav>

<section class="featured">
  <div class="abs hero"></div>
  <div class="abs feature-photo" role="img" aria-label="Plate of wantan noodles with roast pork and bok choy"></div>
  <div class="abs ribbon"><span>Featured</span></div>
  <div class="abs thumb thumb-1" role="img" aria-label="Noodle dish with greens"></div>
  <div class="abs thumb thumb-2" role="img" aria-label="Slices of banana loaf"></div>
  <div class="abs thumb thumb-3" role="img" aria-label="Chilli crab in sauce"></div>
  <div class="abs thumb thumb-4" role="img" aria-label="Tunisian breakfast in a pan"></div>
  <h1 class="abs hero-title" style="font-weight:400">Wantan Mee</h1>
  <p class="abs hero-text">Whenever we are feeling lazy or just want to whip up a quick meal, this is usually one of them. Very fuss free and easy. I taught Lina how to make this once and she's quite good at it now.</p>
</section>

<main>
  <article>
    <div class="abs post-card" style="top:623px"></div>
    <svg class="abs date-badge" style="left:80px;top:647px" viewBox="0 0 82 82">
      <g fill="#e0663a"><circle cx="41" cy="41" r="30"/><circle cx="41" cy="14" r="13"/><circle cx="41" cy="68" r="13"/><circle cx="14" cy="41" r="13"/><circle cx="68" cy="41" r="13"/><circle cx="22" cy="22" r="13"/><circle cx="60" cy="22" r="13"/><circle cx="22" cy="60" r="13"/><circle cx="60" cy="60" r="13"/></g>
      <text x="41" y="36" font-size="21" text-anchor="middle">8</text>
      <text x="41" y="63" font-size="21" text-anchor="middle">Oct</text>
    </svg>
    <h2 class="abs post-title" style="left:169px;top:652px;font-weight:400">Tunisian Breakfast ala Blue Fig</h2>
    <div class="abs post-meta" style="left:167px;top:681px">Posted by <b>Sunny mama</b>, 0 comment</div>
    <div class="abs post-photo" style="left:167px;top:710px" role="img" aria-label="Bread beside a pan of tomato and pepper stew"></div>
    <p class="abs post-excerpt" style="left:329px;top:706px">So I like to do a copycat of the foods which I've eaten outside. Sometimes I can't quite justify paying like $18 for this breakfast when it can be made for only $5 or thereabouts. If you are like me and love the all day Tunisian breakfast at Blue Fig, it must have crossed your <span class="read-more">[Read more]</span></p>
  </article>

  <article>
    <div class="abs post-card" style="top:886px"></div>
    <svg class="abs date-badge" style="left:80px;top:910px" viewBox="0 0 82 82">
      <g fill="#e0663a"><circle cx="41" cy="41" r="30"/><circle cx="41" cy="14" r="13"/><circle cx="41" cy="68" r="13"/><circle cx="14" cy="41" r="13"/><circle cx="68" cy="41" r="13"/><circle cx="22" cy="22" r="13"/><circle cx="60" cy="22" r="13"/><circle cx="22" cy="60" r="13"/><circle cx="60" cy="60" r="13"/></g>
      <text x="41" y="36" font-size="21" text-anchor="middle">8</text>
      <text x="41" y="63" font-size="21" text-anchor="middle">Oct</text>
    </svg>
    <h2 class="abs post-title" style="left:169px;top:915px;font-weight:400">Tunisian Breakfast ala Blue Fig</h2>
    <div class="abs post-meta" style="left:167px;top:944px">Posted by <b>Sunny mama</b>, 0 comment</div>
    <div class="abs post-photo" style="left:167px;top:973px" role="img" aria-label="Bread beside a pan of tomato and pepper stew"></div>
    <p class="abs post-excerpt" style="left:329px;top:969px">So I like to do a copycat of the foods which I've eaten outside. Sometimes I can't quite justify paying like $18 for this breakfast when it can be made for only $5 or thereabouts. If you are like me and love the all day Tunisian breakfast at Blue Fig, it must have crossed your <span class="read-more">[Read more]</span></p>
  </article>
</main>

<aside>
  <h3 class="abs widget-title" style="left:648px;top:628px;font-weight:400">Catagories</h3>
  <ul class="abs widget-list cat-list" style="left:648px;top:658px">
    <li>Bakes</li><li>Breakfast</li><li>Chinese</li><li>Drinks</li><li>Kids</li><li>Musings</li><li>Western</li>
  </ul>

  <h3 class="abs widget-title" style="left:650px;top:826px;font-weight:400">Recent Blog posts</h3>
  <ul class="abs widget-list" style="left:643px;top:860px;width:184px">
    <li>Chestnut Chicken Stew with Carrots and Potatoes</li>
    <li>"Mummy's Favourite Fish Pie"</li>
    <li>Fatty Crab Recipe</li>
    <li>My Breadmaker – Homewell HB100</li>
    <li style="border-bottom:none">Banana Cake/Loaf</li>
  </ul>

  <h3 class="abs widget-title" style="left:645px;top:1012px;font-weight:400">Archives</h3>
  <div class="abs archive-select">Please Select<span class="caret"></span></div>
</aside>

<footer>
  <div class="abs scallop-up"></div>
  <div class="abs site-footer"></div>
  <ul class="footer-nav">
    <li style="left:126px">Home</li>
    <li style="left:178px">About me</li>
    <li style="left:250px">Blog</li>
    <li style="left:299px">Kitchen Tips</li>
    <li style="left:385px">Recipes</li>
    <li style="left:450px">Contact</li>
  </ul>
  <div class="abs copyright">Copyright 2013 www.sunnyoventable.com All Rights Reserved.</div>
</footer>

</body>
</html>
```